Medical Aesthetics business cards

Looking for a business card for my new medical aesthetics business. I am a nurse practitioner and will be administering quilen , fillers as well as providing other services

```html
<!DOCTYPE html>
<html lang="en">
<head>
<meta charset="utf-8">
<title>Mara Ellison – Business Card</title>
<link rel="stylesheet" href="https://fonts.googleapis.com/css2?family=Lato:wght@300;400&family=Montserrat:wght@400&display=swap">
<style>
  :root {
    --backdrop: #e9ebee;
    --card: #ffffff;
    --accent: #e3232b;
    --ink: #2b2b2b;
    --muted: #555555;
    --rule: #1e1e1e;
    --placeholder: #e6e6e6;
  }
  * { box-sizing: border-box; margin: 0; padding: 0; }
  html, body {
    width: 1200px;
    height: 806px;
    overflow: hidden;
    background: var(--backdrop);
  }
  .card {
    position: absolute;
    left: 100px;
    top: 117px;
    width: 1000px;
    height: 572px;
    background: var(--card);
    box-shadow: 0 10px 30px rgba(0, 0, 0, 0.12);
  }
  .card__band {
    position: absolute;
    left: 0;
    right: 0;
    bottom: 0;
    height: 9px;
    background: var(--accent);
  }
  .card__emblem {
    position: absolute;
    left: 340px;
    top: 100px;
    width: 320px;
    height: 160px;
    background: var(--placeholder);
  }
  .identity {
    position: absolute;
    right: 428px;
    top: 372px;
    text-align: right;
  }
  .identity__name {
    font-family: "Montserrat", sans-serif;
    font-weight: 400;
    font-size: 44px;
    line-height: 1;
    color: var(--accent);
    letter-spacing: 0.5px;
  }
  .identity__role {
    font-family: "Lato", sans-serif;
    font-weight: 300;
    font-size: 24px;
    line-height: 1;
    color: var(--ink);
    margin-top: 2px;
    letter-spacing: 0.5px;
  }
  .card__divider {
    position: absolute;
    left: 590px;
    top: 320px;
    width: 2px;
    height: 148px;
    background: var(--rule);
  }
  .contact {
    position: absolute;
    left: 616px;
    top: 322px;
    list-style: none;
    font-family: "Lato", sans-serif;
    font-weight: 300;
    font-size: 22px;
    color: var(--ink);
  }
  .contact__item {
    display: flex;
    align-items: center;
    height: 34px;
  }
  .contact__icon {
    width: 18px;
    height: 18px;
    margin-right: 14px;
    flex: none;
  }
</style>
</head>
<body>
  <main class="card">
    <div class="card__emblem" role="img" aria-label="Nurse cap illustration with a red cross"></div>

    <div class="identity">
      <h1 class="identity__name">Mara Ellison</h1>
      <p class="identity__role">Nurse</p>
    </div>

    <div class="card__divider"></div>

    <ul class="contact">
      <li class="contact__item">
        <svg class="contact__icon" viewBox="0 0 24 24" aria-hidden="true">
          <path fill="var(--accent)" d="M6.6 10.8a15.1 15.1 0 0 0 6.6 6.6l2.2-2.2a1 1 0 0 1 1-.25 11.4 11.4 0 0 0 3.6.57 1 1 0 0 1 1 1V20a1 1 0 0 1-1 1A17 17 0 0 1 3 4a1 1 0 0 1 1-1h3.5a1 1 0 0 1 1 1c0 1.250.2 2.45.57 3.57a1 1 0 0 1-.25 1z"/>
        </svg>
        <span>014 552 3087</span>
      </li>
      <li class="contact__item">
        <svg class="contact__icon" viewBox="0 0 24 24" aria-hidden="true">
          <rect x="2" y="5" width="20" height="14" rx="1.5" fill="var(--accent)"/>
          <path d="M3 6.5l9 6.5 9-6.5" fill="none" stroke="#fff" stroke-width="1.6"/>
        </svg>
        <span>mara.ellison@lumenmail.com</span>
      </li>
      <li class="contact__item">
        <svg class="contact__icon" viewBox="0 0 24 24" aria-hidden="true">
          <circle cx="12" cy="12" r="10" fill="var(--accent)"/>
          <g fill="none" stroke="#fff" stroke-width="1.3">
            <ellipse cx="12" cy="12" rx="4.2" ry="10"/>
            <path d="M2 12h20M4 7h16M4 17h16"/>
          </g>
        </svg>
        <span>www.ellisonclinic.com</span>
      </li>
    </ul>

    <div class="card__band"></div>
  </main>
</body>
</html>
```